I am looking for a flyer design for my upcoming symposium. Here are the details for the flyer and pictures of speakers are attached.

Name of Symposium: Lattice and Pathway Biosciences Symposium, Sponsored by the Corvale Chromatin Institute and the Department of Bioengineering
Date: January 8, 2018
Location: Havergill Auditorium, Tarnby Center for Applied Discovery, 2175 Orchard Terrace Ave, Philadelphia, PA 19127

Reception to follow after the symposium.

Also, please add - Register and upload abstracts for the symposium at www.qzvmrk.com. Registration and abstract submission closes on January 4, 2018.

Keynote Speaker:
Marthe Quillon, Ph.D.
NTVO Director General; Professor, Lyceum of Norvane; Director, Genetics and Developmental Biology at Institut Bramoux
Lyceum of Norvane, NTVO, Institut Bramoux
"Title of talk TBA."

Speakers:
Lena Drewcott, Ph.D.
Assistant Professor of Cell and Developmental Biology
Halvering State University, HMCS
"Title of talk TBA."

Paul Marden, Ph.D.
Assistant Professor of Genetics
"Title of talk TBA."

Ilse Varga, Ph.D.
Professor, Ostrander University
Otto Wenzlau Center for Molecular Medicine
"Title of talk TBA."

Jun Hao, Ph.D.
Professor of Cellular and Molecular Medicine
Coastal Meridian University
"Title of talk TBA."

Wei Lun, Ph.D.
Associate Professor of Pediatrics
The Youth Medical Pavilion of Philadelphia
"Spatial genome re-organization between fetal and adult hematopoietic stem cells."

Mei Zhou, Ph.D.
Professor, Department of Genetics
Ellsworth Medical School
"Title of talk TBA."

```html
<!DOCTYPE html>
<html lang="en">
<head>
<meta charset="utf-8">
<title>Lattice and Pathway Biosciences Symposium</title>
<link rel="stylesheet" href="https://fonts.googleapis.com/css2?family=Roboto:wght@400;500;700;900&family=Saira+Condensed:wght@400;500;600;700&display=swap">
<style>
  :root {
    --bg: #5f6770;
    --paper: #fbfaf6;
    --strip: #efecdf;
    --teal: #1e4d47;
    --orange: #f07c1e;
    --gold: #e8a54a;
    --blue: #2e78b8;
    --ink: #2f2f2f;
    --muted: #3c3c3c;
    --green: #5aaa3c;
  }
  * { margin: 0; padding: 0; box-sizing: border-box; }
  html, body { width: 1200px; height: 1200px; overflow: hidden; background: var(--bg); }
  body { position: relative; font-family: "Roboto", Arial, sans-serif; color: var(--ink); }

  .flyer {
    position: absolute; left: 162px; top: 20px;
    width: 1070px; height: 1416px;
    transform: scale(0.8192); transform-origin: top left;
    background: var(--paper); overflow: hidden;
    box-shadow: 0 4px 14px rgba(0,0,0,.35);
  }
  .top-strip { position: absolute; left: 0; top: 0; width: 100%; height: 25px; background: var(--strip); }

  .title {
    position: absolute; left: 40px; top: 46px; width: 800px;
    font-weight: 900; font-size: 72px; line-height: 82px;
    letter-spacing: -2.5px; color: var(--teal); white-space: nowrap;
  }
  .header-divider { position: absolute; left: 861px; top: 52px; width: 3px; height: 150px; background: var(--orange); }
  .partner { position: absolute; left: 884px; display: flex; align-items: center; gap: 8px;
    font-weight: 700; font-size: 15px; line-height: 17px; color: var(--teal); }
  .partner .mark { width: 18px; height: 18px; border-radius: 50%; background: var(--teal); flex: none; }
  .partner-a { top: 70px; }
  .partner-b { top: 150px; }

  .sponsor { position: absolute; left: 0; width: 990px; top: 222px; text-align: center; font-size: 20px; color: var(--muted); }

  .date { position: absolute; left: 50px; top: 270px; font-family: "Saira Condensed", sans-serif; font-weight: 700; font-size: 33px; color: var(--teal); letter-spacing: .5px; }
  .date span { color: var(--orange); }
  .location { position: absolute; left: 442px; top: 263px; width: 628px; height: 62px; background: var(--blue);
    color: #fff; font-family: "Saira Condensed", sans-serif; font-weight: 500; font-size: 21px; line-height: 25px; padding: 5px 0 0 18px; }
  .location .label { font-weight: 400; }

  .keynote-band { position: absolute; left: 0; top: 325px; width: 100%; height: 360px;
    background: radial-gradient(ellipse at 60% 55%, #f2f5f9 0%, #dfe6ee 55%, #cfd8e3 100%); }
  .portrait-frame { position: absolute; left: 150px; top: 354px; width: 229px; height: 293px; border: 4px solid #111; background: #fff; padding: 6px; }
  .portrait-frame .portrait { width: 100%; height: 100%; border: 4px solid var(--gold);
    background: linear-gradient(160deg, #c9b2a0 0%, #8a6a58 45%, #e6e2de 100%); }
  .keynote-text { position: absolute; left: 400px; width: 555px; top: 378px; text-align: center; }
  .talk-title { font-weight: 700; font-size: 25px; color: #333; }
  .rule { width: 400px; height: 2px; margin: 0 auto; }
  .rule.orange { background: var(--orange); margin-top: 24px; }
  .rule.dark { background: var(--teal); }
  .keynote-label { font-size: 28px; letter-spacing: 1px; color: #222; line-height: 46px; }
  .keynote-label b { font-weight: 900; }
  .keynote-name { font-weight: 700; font-size: 34px; color: var(--orange); margin-top: 10px; }
  .keynote-role { font-size: 19px; line-height: 25px; color: #2a2a2a; margin-top: 4px; }
  .registration { position: absolute; left: 400px; width: 555px; top: 640px; text-align: center;
    font-size: 13px; line-height: 17px; color: var(--teal); font-weight: 500; }

  .speakers-band { position: absolute; left: 0; top: 685px; width: 100%; height: 731px;
    background: radial-gradient(ellipse at 55% 30%, #f3f3f4 0%, #e2e3e6 60%, #d6d8dc 100%); }
  .speakers-tab { position: absolute; left: 0; top: 685px; width: 62px; height: 731px; background: var(--gold); }
  .speakers-tab span { position: absolute; left: 31px; top: 320px; transform: translate(-50%,-50%) rotate(-90deg);
    font-family: "Saira Condensed", sans-serif; font-weight: 700; font-size: 40px; letter-spacing: 1px; color: #fff; white-space: nowrap; }

  .speaker { position: absolute; width: 360px; text-align: center; }
  .speaker .photo-ring { width: 168px; height: 168px; margin: 0 auto; border-radius: 50%; background: #fff; padding: 4px; }
  .speaker .photo { width: 100%; height: 100%; border-radius: 50%; border: 4px solid var(--green);
    background: linear-gradient(160deg, #b58f78 0%, #6e5445 55%, #c9c3bd 100%); }
  .speaker .name { font-weight: 700; font-size: 19px; color: var(--orange); margin-top: 30px; line-height: 24px; }
  .speaker .role { font-size: 14px; line-height: 21px; color: #333; margin-top: 2px; }
  .speaker .talk { font-weight: 700; font-size: 13.5px; line-height: 21px; color: #222; margin-top: 12px; }
  .row-1 { top: 711px; }
  .row-2 { top: 1068px; }
  .row-2 .name { margin-top: 36px; }
  .col-1 { left: 28px; }
  .col-2 { left: 380px; }
  .col-3 { left: 722px; }
</style>
</head>
<body>
<main class="flyer">
  <div class="top-strip"></div>

  <h1 class="title">Lattice and Pathway<br>Biosciences Symposium</h1>
  <div class="header-divider"></div>
  <div class="partner partner-a"><span class="mark"></span>Corvale Chromatin<br>Institute</div>
  <div class="partner partner-b"><span class="mark"></span>Halvering<br>Engineering</div>

  <p class="sponsor">Sponsored by the Corvale Chromatin Institute and the Department of Bioengineering</p>

  <p class="date">DATE : <span>JANUARY 08TH, 2018</span></p>
  <p class="location"><span class="label">Location :</span> Havergill Auditorium, Tarnby Center for Applied Discovery,<br>2175 Orchard Terrace Ave, Philadelphia, PA 19127</p>

  <section class="keynote-band" role="img" aria-label="Soft blue-grey background with a faint DNA double helix"></section>
  <div class="portrait-frame"><div class="portrait" role="img" aria-label="Portrait photo of keynote speaker Marthe Quillon"></div></div>
  <div class="keynote-text">
    <p class="talk-title">"TITLE OF TALK TBA."</p>
    <div class="rule orange"></div>
    <p class="keynote-label"><b>KEYNOTE</b> SPEAKER</p>
    <div class="rule dark"></div>
    <p class="keynote-name">Marthe Quillon, Ph.D.</p>
    <p class="keynote-role">NTVO Director General; Professor, Lyceum of Norvane;<br>Director, Genetics and Developmental Biology at Institut Bramoux<br>Lyceum of Norvane, NTVO, Institut Bramoux</p>
  </div>
  <p class="registration">Register and upload abstracts at www.qzvmrk.com — closes January 4, 2018.<br>Reception to follow after the symposium.</p>

  <section class="speakers-band" role="img" aria-label="Light grey background with a faint DNA double helix"></section>
  <div class="speakers-tab"><span>SPEAKERS</span></div>

  <article class="speaker row-1 col-1">
    <div class="photo-ring"><div class="photo" role="img" aria-label="Photo of Lena Drewcott"></div></div>
    <p class="name">Lena Drewcott, Ph.D.</p>
    <p class="role">Assistant Professor of Cell and<br>Developmental Biology<br>Halvering State University, HMCS</p>
    <p class="talk">“Title of the talk.TBA”</p>
  </article>
  <article class="speaker row-1 col-2">
    <div class="photo-ring"><div class="photo" role="img" aria-label="Photo of Paul Marden"></div></div>
    <p class="name">Paul Marden, Ph.D.</p>
    <p class="role">Assistant Professor of Genetics<br>Halvering State University, HMCS</p>
    <p class="talk" style="margin-top:33px">“Title of the talk.TBA”</p>
  </article>
  <article class="speaker row-1 col-3">
    <div class="photo-ring"><div class="photo" role="img" aria-label="Photo of Ilse Varga"></div></div>
    <p class="name">Ilse Varga, Ph.D.</p>
    <p class="role">Professor, Ostrander University<br>Otto Wenzlau Center for Molecular Medicine</p>
    <p class="talk" style="margin-top:33px">“Title of the talk.TBA”</p>
  </article>

  <article class="speaker row-2 col-1">
    <div class="photo-ring"><div class="photo" role="img" aria-label="Photo of Jun Hao"></div></div>
    <p class="name">Jun Hao, Ph.D.</p>
    <p class="role">Professor of Cellular and Molecular Medicine<br>Coastal Meridian University</p>
    <p class="talk" style="margin-top:4px">“Title of the talk.TBA”</p>
  </article>
  <article class="speaker row-2 col-2">
    <div class="photo-ring"><div class="photo" role="img" aria-label="Photo of Wei Lun"></div></div>
    <p class="name">Wei Lun, Ph.D.</p>
    <p class="role">Associate Professor of Pediatrics<br>The Youth Medical Pavilion of Philadelphia</p>
    <p class="talk" style="margin-top:4px">“Spatial genome re-organization between<br>fetal and adult hematopoietic stem cells.”</p>
  </article>
  <article class="speaker row-2 col-3">
    <div class="photo-ring"><div class="photo" role="img" aria-label="Photo of Mei Zhou"></div></div>
    <p class="name">Mei Zhou, Ph.D.</p>
    <p class="role">Professor, Department of Genetics<br>Ellsworth Medical School</p>
    <p class="talk" style="margin-top:4px">“Title of the talk.TBA”</p>
  </article>
</main>
</body>
</html>
```